Bold Sparrow Studio
Business Cards, Stationary, T-Shirts
Bold Sparrow Studio -
Creative Brief
Use specific fonts
Feel free to use clear fonts
Bright & Fun-filled
Arch. Dave Tuazon
Business Development Manager
Level C, QRT Business Center 482 Willowgate Street Mandaluyong, Metro Manila
tuazon.dave@brightnestinteriors.com
Okay to use single colors in the background with a different color per sheet. Please make format easily editable to change the names and designations of the people on the business cards
Kitchens Closets Storage Solutions

```html
<!DOCTYPE html>
<html lang="en">
<head>
<meta charset="utf-8">
<title>Brightnest Interiors – Stationery Set</title>
<link href="https://fonts.googleapis.com/css2?family=Open+Sans:wght@400;600;800&display=swap" rel="stylesheet">
<style>
  :root{
    --bg:#e7e4df;
    --paper:#ffffff;
    --blue:#1f4f8f;
    --blue-light:#3a7bc8;
    --green:#2f8a2c;
    --green-light:#9bd23a;
    --ink:#3b3b3b;
    --muted:#8a8f96;
    --line:#c7d2e0;
    --faint:#eef1f5;
  }
  *{box-sizing:border-box;margin:0;padding:0}
  html,body{width:1200px;height:576px;overflow:hidden}
  body{background:var(--bg);font-family:"Open Sans",Arial,sans-serif;color:var(--ink);position:relative}
  .piece{position:absolute;background:var(--paper);box-shadow:0 2px 6px rgba(0,0,0,.25);overflow:hidden}
  .brand{display:flex;align-items:center;gap:4px;font-weight:800;color:var(--blue);letter-spacing:.5px}
  .brand .mark{width:14px;height:14px;background:var(--blue)}
  .brand.on-dark{color:#fff}
  .brand.on-dark .mark{background:#fff}
  .tiny{font-size:5px;line-height:1.35}
  .small{font-size:6px;line-height:1.4}

  /* business cards */
  .card{width:134px;height:96px}
  .card-front{left:53px;top:67px;padding:8px}
  .card-front .name{font-size:7px;font-weight:800;color:var(--blue)}
  .card-front .title{font-size:5px;color:var(--muted);margin-bottom:5px}
  .card-front .brand{position:absolute;right:7px;top:7px;font-size:6px}
  .card-front .brand .mark{width:8px;height:8px}
  .card-front .band{position:absolute;left:0;right:0;bottom:0;height:10px;background:linear-gradient(90deg,var(--blue),var(--blue-light))}
  .card-blue{left:197px;top:67px;width:139px;background:radial-gradient(circle at 50% 40%,var(--blue-light),var(--blue));display:flex;flex-direction:column;align-items:center;justify-content:center;gap:3px}
  .card-green{left:53px;top:173px;background:radial-gradient(circle at 50% 40%,var(--green-light),var(--green));display:flex;align-items:center;justify-content:center}
  .card-white{left:197px;top:173px;width:139px;display:flex;align-items:center;justify-content:center}
  .card-blue .brand,.card-green .brand,.card-white .brand{font-size:11px}
  .tagline{font-size:4.5px;color:#dfe9f7;letter-spacing:.5px}

  /* envelope flap strip */
  .env-strip{left:197px;top:283px;width:139px;height:41px;background:linear-gradient(90deg,var(--blue),var(--blue-light))}
  .env-strip svg{position:absolute;left:0;top:0}

  /* envelope */
  .envelope{left:53px;top:336px;width:283px;height:144px}
  .envelope .flap{position:absolute;left:0;top:0}
  .envelope .brand{position:absolute;left:12px;top:52px;font-size:8px}
  .envelope .brand .mark{width:9px;height:9px}
  .envelope .return{position:absolute;left:12px;top:66px}

  /* compliment slip */
  .slip{left:72px;top:492px;width:264px;height:65px}
  .slip .head{height:20px;display:flex;align-items:center;gap:10px;padding:0 8px;border-bottom:3px solid var(--blue)}
  .slip .brand{font-size:8px}
  .slip .brand .mark{width:9px;height:9px}
  .slip .greeting{padding:6px 8px;color:var(--muted)}

  /* letter sheets */
  .sheet{top:43px;width:247px;height:497px}
  .letterhead{left:456px}
  .fax{left:720px;width:245px}
  .sheet-head{height:48px;background:linear-gradient(90deg,var(--paper) 0 30%,var(--blue) 30%,var(--blue-light));display:flex;align-items:center;gap:8px;padding:0 8px}
  .sheet-head .brand{width:66px;font-size:8px;flex-direction:column;gap:2px}
  .sheet-head .brand .mark{width:14px;height:14px}
  .sheet-head .contact{color:#fff;font-size:4.5px;line-height:1.4;flex:1}
  .watermark{position:absolute;left:50%;top:58%;transform:translate(-50%,-50%);width:130px;height:130px;background:var(--faint)}
  .fax-table{margin:12px 10px 0;border:1px solid var(--line);font-size:5px}
  .fax-title{background:var(--blue);color:#fff;font-weight:800;font-size:10px;padding:3px 6px}
  .fax-row{display:flex;border-top:1px solid var(--line);height:10px}
  .fax-row span{flex:1;padding:1px 4px;border-right:1px solid var(--line)}
  .fax-row span:last-child{border-right:0}
  .fax-checks{display:flex;gap:8px;margin:8px 10px 0;font-size:4.5px;color:var(--muted)}
  .fax-checks i{display:inline-block;width:4px;height:4px;border:1px solid var(--muted);margin-right:2px;vertical-align:middle}
  .fax-comments{margin:6px 10px;font-size:4.5px;color:var(--muted)}
</style>
</head>
<body>

<!-- business card: contact side -->
<div class="piece card card-front">
  <div class="brand"><span class="mark"></span>BRIGHTNEST</div>
  <div class="name">Dave Tuazon</div>
  <div class="title">Business Development Manager</div>
  <div class="tiny">Level C, QRT Business Center<br>482 Willowgate Street<br>Mandaluyong, Metro Manila</div>
  <div class="tiny" style="margin-top:3px">T: +63 2 555 0184<br>tuazon.dave@brightnestinteriors.com</div>
  <div class="band"></div>
</div>

<!-- business card: blue side -->
<div class="piece card card-blue">
  <div class="brand on-dark"><span class="mark"></span>BRIGHTNEST</div>
  <div class="tagline">KITCHENS · CLOSETS · STORAGE SOLUTIONS</div>
</div>

<!-- business card: green side -->
<div class="piece card card-green">
  <div class="brand on-dark"><span class="mark"></span>BRIGHTNEST</div>
</div>

<!-- business card: white side -->
<div class="piece card card-white">
  <div class="brand"><span class="mark"></span>BRIGHTNEST</div>
</div>

<!-- envelope flap -->
<div class="piece env-strip">
  <svg width="139" height="41"><polygon points="0,0 139,0 139,10 69.5,34 0,10" fill="#fff" opacity=".15"/><rect x="62" y="10" width="15" height="15" fill="#fff"/></svg>
</div>

<!-- envelope -->
<div class="piece envelope">
  <svg class="flap" width="283" height="40">
    <defs><linearGradient id="flapGreen" x1="0" x2="1"><stop offset="0" stop-color="#2f8a2c"/><stop offset="1" stop-color="#9bd23a"/></linearGradient></defs>
    <polygon points="0,0 283,0 283,14 141.5,40 0,14" fill="url(#flapGreen)"/>
  </svg>
  <div class="brand"><span class="mark"></span>BRIGHTNEST</div>
  <div class="tiny return">Level C, QRT Business Center<br>482 Willowgate Street, Mandaluyong</div>
</div>

<!-- compliment slip -->
<div class="piece slip">
  <div class="head">
    <div class="brand"><span class="mark"></span>BRIGHTNEST</div>
    <div class="tiny">Level C, QRT Business Center, 482 Willowgate Street<br>T: +63 2 555 0184 · brightnestinteriors.com</div>
  </div>
  <div class="small greeting">With Compliments</div>
</div>

<!-- letterhead -->
<div class="piece sheet letterhead">
  <div class="sheet-head">
    <div class="brand"><span class="mark"></span>BRIGHTNEST</div>
    <div class="contact">Level C, QRT Business Center<br>482 Willowgate Street<br>Mandaluyong, Metro Manila</div>
    <div class="contact">T: +63 2 555 0184<br>F: +63 2 555 0185<br>brightnestinteriors.com</div>
  </div>
  <div class="watermark"></div>
</div>

<!-- fax sheet -->
<div class="piece sheet fax">
  <div class="sheet-head">
    <div class="brand"><span class="mark"></span>BRIGHTNEST</div>
    <div class="contact">Level C, QRT Business Center<br>482 Willowgate Street<br>Mandaluyong, Metro Manila</div>
    <div class="contact">T: +63 2 555 0184<br>F: +63 2 555 0185<br>brightnestinteriors.com</div>
  </div>
  <div class="fax-table">
    <div class="fax-title">FAX</div>
    <div class="fax-row"><span>To:</span><span>From:</span></div>
    <div class="fax-row"><span>Fax:</span><span>Pages:</span></div>
    <div class="fax-row"><span>Phone:</span><span>Date:</span></div>
    <div class="fax-row"><span>Re:</span><span>CC:</span></div>
  </div>
  <div class="fax-checks"><span><i></i>Urgent</span><span><i></i>For Review</span><span><i></i>Please Comment</span><span><i></i>Please Reply</span></div>
  <div class="fax-comments">Comments:</div>
  <div class="watermark"></div>
</div>

</body>
</html>
```